Redesign for a start up airline technology. The website is tembrulon.com.

I need a PowerPoint template that complements our website. I can provide our current template as a starting point.

```html
<!DOCTYPE html>
<html lang="en">
<head>
<meta charset="utf-8">
<title>Tembrulon Presentation Template</title>
<link href="https://fonts.googleapis.com/css2?family=Montserrat:wght@400;500;700;800&display=swap" rel="stylesheet">
<style>
  :root {
    --canvas: #dcdadb;
    --white: #ffffff;
    --navy: #0b3f8b;
    --navy-deep: #0a3d86;
    --ocean: #0b7ab6;
    --teal-deep: #0b5571;
    --green: #5ab92e;
    --green-light: #c8ee8c;
    --ink: #222831;
    --muted: #55606c;
  }
  * { box-sizing: border-box; margin: 0; padding: 0; }
  html, body {
    width: 1200px; height: 2765px; overflow: hidden;
    background: var(--canvas);
    font-family: "Montserrat", sans-serif;
  }
  .canvas { position: relative; width: 1200px; height: 2765px; }

  .slide {
    position: absolute; left: 60px;
    width: 1080px; height: 607px;
    background: var(--white); overflow: hidden;
  }
  .slide--preview { left: 159px; top: 86px; transform: scale(0.815); transform-origin: 0 0; }
  .slide--title { top: 845px; }
  .slide--content { top: 1470px; }
  .slide--closing { top: 2095px; }

  .brand-name {
    position: absolute; left: 74px; top: 46px;
    font-weight: 800; font-size: 50px; letter-spacing: 1px;
    color: var(--navy);
  }
  .band {
    position: absolute; left: 0; top: 132px; width: 1080px; height: 429px;
    background: linear-gradient(90deg, var(--navy-deep) 0%, #0a4f98 40%, var(--ocean) 100%);
  }
  .band--closing {
    background: linear-gradient(90deg, var(--navy-deep) 0%, #0a4a88 45%, var(--teal-deep) 100%);
  }
  .band-art {
    position: absolute; left: 380px; top: 0; width: 700px; height: 429px;
    background:
      radial-gradient(circle at 56% 88%, rgba(40,150,220,0.55) 0 18%, transparent 19%),
      radial-gradient(circle at 56% 88%, rgba(60,160,230,0.25) 0 42%, transparent 43%),
      linear-gradient(90deg, rgba(20,110,190,0) 0%, rgba(20,130,200,0.35) 100%);
  }
  .band-art--globe {
    left: 360px; width: 720px;
    background:
      radial-gradient(ellipse at 50% 100%, rgba(70,150,190,0.35) 0 45%, transparent 60%),
      linear-gradient(90deg, rgba(10,70,130,0) 0%, rgba(10,90,115,0.4) 100%);
  }
  .title-block { position: absolute; left: 113px; top: 95px; color: var(--white); }
  .title-block h1 {
    font-weight: 800; font-size: 60px; line-height: 66px; letter-spacing: 2px;
  }
  .title-block .subtitle { margin-top: 12px; font-size: 27px; font-weight: 400; letter-spacing: 0.3px; }
  .title-block .date { margin-top: 42px; font-size: 14px; font-weight: 500; }

  .footer-note {
    position: absolute; left: 0; right: 0; top: 574px;
    text-align: center; font-size: 11.5px; color: var(--muted);
  }

  /* content slide */
  .content-heading {
    position: absolute; left: 59px; top: 48px;
    font-weight: 800; font-size: 35px; letter-spacing: 0.8px; color: var(--navy);
  }
  .accent-bar {
    position: absolute; left: 62px; top: 98px; width: 92px; height: 13px; border-radius: 7px;
    background: linear-gradient(90deg, var(--green) 0%, var(--green-light) 70%, rgba(230,250,200,0) 100%);
  }
  .brand-name--small {
    left: auto; right: 42px; top: 62px; font-size: 26px; letter-spacing: 0.5px;
  }
  .body-copy {
    position: absolute; left: 59px; top: 157px; width: 972px;
    font-size: 13.4px; line-height: 14.7px; color: var(--ink); text-align: justify;
  }
  .body-copy p + p { margin-top: 10px; }
  .confidential { position: absolute; left: 30px; top: 560px; font-size: 12px; color: var(--ink); font-weight: 500; }
  .rights { position: absolute; right: 65px; top: 561px; font-size: 12px; color: var(--muted); }
  .page-number {
    position: absolute; left: 1030px; top: 557px; width: 20px; height: 20px; border-radius: 4px;
    background: var(--navy); color: var(--white); font-size: 10px; line-height: 20px; text-align: center;
  }

  /* closing slide */
  .closing-block { position: absolute; left: 120px; top: 92px; color: var(--white); }
  .closing-block h2 { font-weight: 800; font-size: 48px; letter-spacing: 1.5px; }
  .closing-block h3 { margin-top: 40px; font-weight: 700; font-size: 20px; letter-spacing: 1.5px; }
  .contact-list { list-style: none; margin-top: 20px; }
  .contact-list li { display: flex; align-items: center; height: 31px; font-size: 16px; }
  .contact-list svg { width: 22px; height: 22px; margin-right: 13px; }
</style>
</head>
<body>
<main class="canvas">

  <section class="slide slide--preview" aria-label="Title slide preview">
    <div class="brand-name">Tembrulon</div>
    <div class="band">
      <div class="band-art" role="img" aria-label="Faint blueprint drawing of an aircraft engine with grid lines"></div>
      <div class="title-block">
        <h1>Presentation<br>Title Goes Here</h1>
        <p class="subtitle">Subtitle of Presentation Goes Here</p>
        <p class="date">Wednesday, May 29, 2024</p>
      </div>
    </div>
    <p class="footer-note">© Tembrulon, LLC. All Rights Reserved.</p>
  </section>

  <section class="slide slide--title" aria-label="Title slide">
    <div class="brand-name">Tembrulon</div>
    <div class="band">
      <div class="band-art" role="img" aria-label="Faint blueprint drawing of an aircraft engine with grid lines"></div>
      <div class="title-block">
        <h1>Presentation<br>Title Goes Here</h1>
        <p class="subtitle">Subtitle of Presentation Goes Here</p>
        <p class="date">Wednesday, May 29, 2024</p>
      </div>
    </div>
    <p class="footer-note">© Tembrulon, LLC. All Rights Reserved.</p>
  </section>

  <section class="slide slide--content" aria-label="Content slide">
    <h2 class="content-heading">Heading Goes Here</h2>
    <div class="accent-bar"></div>
    <div class="brand-name brand-name--small">Tembrulon</div>
    <div class="body-copy">
      <p>Lorem ipsum dolor sit amet, consectetur adipiscing elit. Vivamus eu dui ex. Curabitur dapibus dignissim dui, in molestie metus feugiat sed. Praesent aliquet lorem ex, eu dapibus odio varius at. Duis eget tellus porta, consequat lacus vitae, venenatis dolor. Nulla facilisi. In et sollicitudin lacus. Donec risus orci, gravida sit amet risus vehicula, aliquet pretium sapien. Nullam sit amet magna non ex bibendum mollis. Nunc vel neque eu augue dignissim congue ut vitae magna. Phasellus eget commodo arcu. Nunc vitae semper dui. Integer venenatis, tellus sit amet interdum pretium, erat neque rhoncus turpis, a aliquam augue ligula eget erat. Nunc placerat, arcu nec mattis fermentum, nisi mauris convallis nunc, ut luctus nunc nisl id ex. Nam semper tristique mauris, et vestibulum leo fringilla vel. Nulla id augue eleifend, egestas ligula et, consequat massa. Pellentesque habitant morbi tristique senectus et netus et malesuada fames ac turpis egestas.</p>
      <p>Lorem ipsum dolor sit amet, consectetur adipiscing elit. Vivamus eu dui ex. Curabitur dapibus dignissim dui, in molestie metus feugiat sed. Praesent aliquet lorem ex, eu dapibus odio varius at. Duis eget tellus porta, consequat lacus vitae, venenatis dolor. Nulla facilisi. In et sollicitudin lacus. Donec risus orci, gravida sit amet risus vehicula, aliquet pretium sapien. Nullam sit amet magna non ex bibendum mollis. Nunc vel neque eu augue dignissim congue ut vitae magna. Phasellus eget commodo arcu. Nunc vitae semper dui. Integer venenatis, tellus sit amet interdum pretium, erat neque rhoncus turpis, a aliquam augue ligula eget erat. Nunc placerat, arcu nec mattis fermentum, nisi mauris convallis nunc, ut luctus nunc nisl id ex. Nam semper tristique mauris, et vestibulum leo fringilla vel. Nulla id augue eleifend, egestas ligula et, consequat massa. Pellentesque habitant morbi tristique senectus et netus et malesuada fames ac turpis egestas.</p>
      <p>Lorem ipsum dolor sit amet, consectetur adipiscing elit. Vivamus eu dui ex. Curabitur dapibus dignissim dui, in molestie metus feugiat sed. Praesent aliquet lorem ex, eu dapibus odio varius at. Duis eget tellus porta, consequat lacus vitae, venenatis dolor. Nulla facilisi. In et sollicitudin lacus. Donec risus orci, gravida sit amet risus vehicula, aliquet pretium sapien. Nullam sit amet magna non ex bibendum mollis.</p>
      <p>Lorem ipsum dolor sit amet, consectetur adipiscing elit. Vivamus eu dui ex. Curabitur dapibus dignissim dui, in molestie metus feugiat sed. Praesent aliquet lorem ex, eu dapibus odio varius at. Duis eget tellus porta, consequat lacus vitae, venenatis dolor. Nulla facilisi. In et sollicitudin lacus. Donec risus orci, gravida sit amet risus vehicula, aliquet pretium sapien. Nullam sit amet magna non ex bibendum mollis. Nunc vel neque eu augue dignissim congue ut vitae magna. Phasellus eget commodo arcu. Nunc vitae semper dui. Integer venenatis, tellus sit amet interdum pretium, erat neque rhoncus turpis, a aliquam augue ligula eget erat.</p>
    </div>
    <p class="confidential">Confidential and Proprietary</p>
    <p class="rights">© Tembrulon, LLC. All Rights Reserved.</p>
    <div class="page-number">2</div>
  </section>

  <section class="slide slide--closing" aria-label="Closing slide">
    <div class="brand-name">Tembrulon</div>
    <div class="band band--closing">
      <div class="band-art band-art--globe" role="img" aria-label="Faint globe with a network of flight route lines"></div>
      <div class="closing-block">
        <h2>Thank You!</h2>
        <h3>Contact Us</h3>
        <ul class="contact-list">
          <li>
            <svg viewBox="0 0 24 24" fill="none" stroke="#fff" stroke-width="2" stroke-linecap="round" stroke-linejoin="round" aria-hidden="true"><path d="M5 3h4l2 5-2.5 1.5a11 11 0 0 0 6 6L16 13l5 2v4a2 2 0 0 1-2 2A16 16 0 0 1 3 5a2 2 0 0 1 2-2z"/></svg>
            555-0134-1222
          </li>
          <li>
            <svg viewBox="0 0 24 24" fill="none" stroke="#fff" stroke-width="2.2" stroke-linecap="round" aria-hidden="true"><circle cx="12" cy="12" r="4"/><path d="M16 8v5a3 3 0 0 0 6 0v-1a10 10 0 1 0-4 8"/></svg>
            info@tembrulon.com
          </li>
          <li>
            <svg viewBox="0 0 24 24" fill="none" stroke="#fff" stroke-width="1.8" aria-hidden="true"><circle cx="12" cy="12" r="10"/><ellipse cx="12" cy="12" rx="4.5" ry="10"/><path d="M2 12h20M4 7h16M4 17h16"/></svg>
            https://www.tembrulon.com
          </li>
        </ul>
      </div>
    </div>
    <p class="footer-note">© Tembrulon, LLC. All Rights Reserved.</p>
  </section>

</main>
</body>
</html>
```